Room 4 Keeps Storage Poster Ad

Room 4 Keeps Storage needs an 8.5" X 11" specialty storage products poster.

Graphics that illustrate seasonal tire storage, bicycle storage, and motorcycle storage.

Information on the poster will be as follows:

Tire storage: $99.00/season + tax
bicycle storage: $99.00/season + tax
motorcycle storage: $250.00/season + tax
Phone: 306-517-4832
Web: www.room4keeps.ca
Address: Room 4 Keeps Storage, 4178 Draven Avenue, Saskatoon, SK, S7M 2R4

**Information does not need to be presented in this exact format. The designer can creatively list the services and the prices. The words phone, web, and address can be left out**

**The season that the ad is targeting is winter

Industry/Entity Type

Storage

```html
<!DOCTYPE html>
<html lang="en">
<head>
<meta charset="utf-8">
<title>Room 4 Keeps Storage – Winter Storage Poster</title>
<link href="https://fonts.googleapis.com/css2?family=Anton&family=Roboto:wght@700;900&family=Questrial&display=swap" rel="stylesheet">
<style>
  :root {
    --backdrop: #000000;
    --gold: #f9cb3a;
    --cream: #fff9d6;
    --red: #d7262b;
    --ink: #231f20;
    --white: #ffffff;
    --band: #111111;
    --tire-a: #5f6b73;
    --tire-b: #a9b4bb;
    --bike: #1c1c1c;
    --moto-a: #2a2d33;
    --moto-b: #6b7280;
  }
  * { box-sizing: border-box; margin: 0; padding: 0; }
  html, body {
    width: 946px; height: 1200px; overflow: hidden;
    background: var(--backdrop);
  }
  .canvas { position: relative; width: 946px; height: 1200px; }
  .poster {
    position: absolute; left: 84px; top: 96px; width: 778px; height: 1008px;
    background: linear-gradient(90deg, var(--gold) 0%, var(--cream) 48%, var(--cream) 55%, var(--gold) 100%);
    overflow: hidden;
  }
  .abs { position: absolute; }

  .brand {
    left: 0; width: 100%; top: 170px; text-align: center;
    font-family: "Roboto", sans-serif; font-weight: 900; color: var(--ink);
    letter-spacing: 1px; line-height: 1.05;
  }
  .brand .brand-line { display: block; font-size: 40px; }
  .brand .brand-line.sub { font-size: 36px; letter-spacing: 3px; }

  .ribbon {
    height: 43px; background: var(--red); color: var(--white);
    font-family: "Roboto", sans-serif; font-weight: 900; font-size: 27px;
    line-height: 43px; padding-left: 12px; letter-spacing: .3px;
    clip-path: polygon(0 0, 100% 0, calc(100% - 16px) 50%, 100% 100%, 0 100%);
  }
  .price {
    font-family: "Anton", sans-serif; font-size: 60px; line-height: 1;
    color: var(--ink); letter-spacing: .5px;
  }
  .price-note {
    font-family: "Questrial", sans-serif; font-size: 18px; color: var(--ink);
    letter-spacing: .5px;
  }

  .art { border-radius: 14px; }
  .art-tires { background: radial-gradient(ellipse at 45% 50%, var(--tire-b), var(--tire-a) 75%, transparent 76%); }
  .art-bike { background: radial-gradient(ellipse at 50% 55%, var(--bike) 0%, #3a3a3a 55%, transparent 72%); }
  .art-moto { background: radial-gradient(ellipse at 50% 55%, var(--moto-b) 0%, var(--moto-a) 55%, transparent 72%); }

  .services-band {
    left: 0; top: 780px; width: 100%; height: 32px; background: var(--band);
    color: var(--white); font-family: "Roboto", sans-serif; font-weight: 700;
    font-size: 15px; line-height: 32px; text-align: center; letter-spacing: .3px;
  }
  .contact { left: 0; width: 100%; text-align: center; }
  .address, .web {
    font-family: "Questrial", sans-serif; font-size: 20px; color: var(--ink);
    letter-spacing: .5px;
  }
  .address { top: 824px; }
  .web { top: 850px; }
  .phone {
    top: 872px; font-family: "Roboto", sans-serif; font-weight: 900;
    font-size: 56px; color: var(--red); letter-spacing: 1px;
  }
  .promise-bar {
    left: 168px; top: 944px; width: 440px; height: 36px; background: var(--band);
    color: var(--white); font-family: "Roboto", sans-serif; font-weight: 900;
    font-size: 23px; line-height: 36px; text-align: center; letter-spacing: .5px;
  }
</style>
</head>
<body>
<main class="canvas">
  <section class="poster">
    <h1 class="abs brand">
      <span class="brand-line">ROOM 4 KEEPS</span>
      <span class="brand-line sub">STORAGE</span>
    </h1>

    <div class="abs art art-tires" style="left:113px;top:274px;width:273px;height:130px" role="img" aria-label="Stack of four car tires"></div>
    <div class="abs ribbon" style="left:416px;top:277px;width:248px">Tire Storage</div>
    <div class="abs price" style="left:427px;top:328px">$99.00</div>
    <div class="abs price-note" style="left:427px;top:389px">per season+tax</div>

    <div class="abs ribbon" style="left:137px;top:462px;width:290px">Bicycle Storage</div>
    <div class="abs price" style="left:149px;top:513px">$99.00</div>
    <div class="abs price-note" style="left:149px;top:573px">per season+tax</div>
    <div class="abs art art-bike" style="left:428px;top:416px;width:204px;height:193px" role="img" aria-label="Black bicycle silhouette"></div>

    <div class="abs art art-moto" style="left:71px;top:607px;width:266px;height:143px" role="img" aria-label="Black sport motorcycle"></div>
    <div class="abs ribbon" style="left:350px;top:622px;width:354px">Motorcycle Storage</div>
    <div class="abs price" style="left:363px;top:674px">$250.00</div>
    <div class="abs price-note" style="left:363px;top:733px">per season+tax</div>

    <div class="abs services-band">Specialty storage products • Moving truck rental • Online booking and payments</div>

    <p class="abs contact address">4178 Draven ave, Saskatoon, SK, S7M 2R4</p>
    <p class="abs contact web">www.room4keeps.ca</p>
    <p class="abs contact phone">306-517-4832</p>
    <div class="abs promise-bar">Safe | Secure | 24hr Access</div>
  </section>
</main>
</body>
</html>
```